Flyer Design Project

We are offering a new class on cyber crime and want to advertise this course to students. We would like to see a design that is eye catching and coveys the goals of the course, when it meets and a brief abstract for the class.

The course will focus on the economics of cyber crime so including one or two graphics that get across this point would be good.

Requirements
Must have
• Course name "Cyber Crime"
Call number "CS 795 - 004"
Course meeting time (day of week and time) Tue. 4:30-7:10pm
Course goals
Course abstract

```html
<!DOCTYPE html>
<html lang="en">
<head>
<meta charset="utf-8">
<title>Cyber Crimes – Fall 2012 Course Flyer</title>
<link rel="stylesheet" href="https://fonts.googleapis.com/css2?family=Carlito:ital,wght@0,400;0,700;1,400&family=Share+Tech+Mono&display=swap">
<style>
  :root {
    --page-frame: #a3a3a3;
    --page-bg: #000000;
    --title-green: #33ff2e;
    --title-glow: rgba(60, 255, 60, 0.55);
    --info-yellow: #f2f200;
    --heading-red: #ff1a0f;
    --body-white: #ffffff;
    --logo-blue: #1a2be8;
    --logo-text: #000000;
    --money-dark: #0b0d0b;
    --money-mid: #262b24;
    --hero-light: #8a8a8a;
    --hero-dark: #2c2c2c;
  }
  * { box-sizing: border-box; margin: 0; padding: 0; }
  html, body {
    width: 933px;
    height: 1200px;
    overflow: hidden;
    background: var(--page-frame);
  }
  .flyer {
    position: relative;
    width: 933px;
    height: 1200px;
    border: 10px solid var(--page-frame);
    background: var(--page-bg);
    overflow: hidden;
    font-family: "Carlito", "Calibri", sans-serif;
    color: var(--body-white);
  }
  .money-backdrop {
    position: absolute;
    left: 0; right: 0; top: 640px; bottom: 0;
    background: radial-gradient(ellipse at 60% 70%, var(--money-mid) 0%, var(--money-dark) 55%, var(--page-bg) 100%);
  }
  .title {
    position: absolute;
    top: 22px; left: 0; right: 0;
    text-align: center;
    font-family: "Share Tech Mono", monospace;
    font-weight: 400;
    font-size: 94px;
    letter-spacing: 17px;
    padding-left: 17px;
    color: var(--title-green);
    text-shadow: 0 0 10px var(--title-glow), 0 0 3px var(--title-glow);
    line-height: 1;
  }
  .course-info {
    position: absolute;
    top: 143px; left: 0; right: 0;
    text-align: center;
    font-family: "Share Tech Mono", monospace;
    font-size: 40px;
    letter-spacing: 4px;
    line-height: 43px;
    color: var(--info-yellow);
  }
  .section-heading {
    color: var(--heading-red);
    font-weight: 700;
    font-size: 22px;
    text-align: center;
    line-height: 1;
  }
  .abstract {
    position: absolute;
    top: 318px; left: 4px; right: 4px;
  }
  .abstract p {
    margin-top: 5px;
    font-style: italic;
    font-size: 20.5px;
    line-height: 27px;
    text-align: center;
  }
  .goals {
    position: absolute;
    top: 567px; left: 4px; right: 4px;
  }
  .goals ol {
    list-style: none;
    margin-top: 5px;
    font-style: italic;
    font-size: 20.5px;
    line-height: 25px;
    text-align: center;
  }
  .hero-art {
    position: absolute;
    left: 25px; top: 672px;
    width: 585px; height: 443px;
    background: linear-gradient(160deg, var(--hero-dark) 0%, var(--hero-light) 55%, var(--hero-dark) 100%);
  }
  .college-mark {
    position: absolute;
    left: 636px; top: 932px;
    width: 259px; height: 134px;
    background: var(--logo-blue);
    display: flex;
    align-items: center;
    justify-content: center;
    font-style: italic;
    font-size: 16px;
    color: var(--logo-text);
  }
  .more-info {
    position: absolute;
    right: 4px; top: 1110px;
    text-align: right;
    font-family: "Share Tech Mono", monospace;
    font-size: 24px;
    line-height: 31px;
    letter-spacing: 1px;
    color: var(--body-white);
  }
</style>
</head>
<body>
  <main class="flyer">
    <div class="money-backdrop" role="img" aria-label="Faded photograph of scattered dollar bills"></div>

    <h1 class="title">CYBER CRIMES</h1>

    <div class="course-info">
      <p>for Fall 2012</p>
      <p>Course CS 795 / ISA 797</p>
      <p>Tuesdays 4:30 – 7:10 PM</p>
    </div>

    <section class="abstract">
      <h2 class="section-heading">Course Abstract</h2>
      <p>Arguably the single most significant change in the cyber-security landscape has been the explo-<br>sive rise of profit-fueled cyber-crime. Obtaining a detailed, structural understanding of how<br>profit-driven cyber crime works — its underlying economics and associated business practices<br>— has the potential to illuminate new defensive measures that might prove far more efficient<br>for countering attacks than purely technical measures. This research seminar will delve into our<br>current understanding of the economics of cyber-crime.</p>
    </section>

    <section class="goals">
      <h2 class="section-heading">Course Goals</h2>
      <ol>
        <li>1) Understand how modern cyber-crime operates on a technical and economic level</li>
        <li>2) Analyze some of the potential places to intervene at an economic, technical and policy level.</li>
      </ol>
    </section>

    <div class="hero-art" role="img" aria-label="Photograph of an open silver laptop with a magnifying glass revealing a fingerprint"></div>

    <div class="college-mark">COLLEGE LOGO</div>

    <div class="more-info">
      <p>For More Information, visit:</p>
      <p>http://cs.northfield.edu/~harlow/crime.html</p>
    </div>
  </main>
</body>
</html>
```